Lawn care business card

I am looking for a quality designed personal business card to represent the quality and elegant nature of our company. We separate ourselves in our market by the aesthetic value of our work, so I am looking for marketing material that does the same. We target our marketing high end customers, and we try to avoid price shoppers. I am open to all design options, so long as they are in line with our companies values.

We are tend to go with a retro look on everything from our logo and print material, to our uniforms. We like to portray and "old fashion" set of core values, with a modern elegance. So a wild and crazy look is out of the question.

Things I'd like on the card:
1.) Logo
2.) Phone number: (816) 555-0193
3.) Website: Verdanthollow.com
4.) Email: peterwalsh@verdanthollow.com
5.) My name: Peter Walsh
6.) Facebook link: facebook.com/GreenridgeLawnandLandscape
7.) Instagram: http://instagram.com/verdanthollow

Attached is a copy of our logo.

```html
<!DOCTYPE html>
<html lang="en">
<head>
<meta charset="utf-8">
<title>Verdant Hollow – Business Card</title>
<link rel="stylesheet" href="https://fonts.googleapis.com/css2?family=Roboto+Slab:wght@300;400;500&display=swap">
<style>
  :root {
    --backdrop: #6e7174;
    --card: #f3f3f1;
    --ink: #1f1f1f;
    --ink-soft: #333333;
    --accent: #e8622a;
  }
  * { box-sizing: border-box; margin: 0; padding: 0; }
  html, body {
    width: 1200px; height: 900px; overflow: hidden;
    background: var(--backdrop);
  }
  .stage {
    width: 1200px; height: 900px;
    display: flex; align-items: center; justify-content: center;
  }
  .card {
    width: 440px; height: 770px;
    background: var(--card);
    color: var(--ink);
    font-family: "Roboto Slab", Georgia, serif;
    display: flex; flex-direction: column; align-items: center;
    padding: 78px 48px 52px;
    box-shadow: 0 6px 24px rgba(0,0,0,.25);
  }
  .brand {
    display: flex; align-items: center; gap: 14px;
    white-space: nowrap;
  }
  .brand-dot {
    width: 44px; height: 44px; border-radius: 50%;
    background: var(--accent); flex: none;
  }
  .brand-name {
    font-size: 28px; font-weight: 500; letter-spacing: 1px;
    text-transform: uppercase; color: var(--ink);
  }
  .person-name {
    margin-top: 150px;
    font-size: 26px; font-weight: 400; letter-spacing: .5px;
    text-transform: uppercase; white-space: nowrap;
  }
  .divider-cross { margin: 12px 0 8px; }
  .contact { align-self: stretch; text-align: center; }
  .phone { font-size: 42px; font-weight: 400; line-height: 1.1; white-space: nowrap; }
  .email { font-size: 17px; font-weight: 300; margin-top: 14px; color: var(--ink-soft); white-space: nowrap; }
  .social { align-self: stretch; margin-top: 26px; padding-left: 4px; }
  .social-row {
    display: flex; align-items: center; gap: 10px;
    font-size: 16px; font-weight: 300; color: var(--ink-soft);
    margin-bottom: 10px; white-space: nowrap;
  }
  .social-mark { width: 22px; height: 22px; background: var(--ink); flex: none; }
  .rule { align-self: stretch; margin-top: 10px; }
  .rule-thick { height: 3px; background: var(--ink); }
  .rule-thin { height: 1px; background: var(--ink); margin-top: 3px; }
  .website {
    margin-top: 18px; font-size: 30px; font-weight: 400;
    text-transform: uppercase; letter-spacing: .3px; white-space: nowrap;
  }
</style>
</head>
<body>
<main class="stage">
  <article class="card">
    <header class="brand">
      <span class="brand-dot"></span>
      <span class="brand-name">Verdant Hollow</span>
    </header>

    <h1 class="person-name">Peter Walsh</h1>
    <svg class="divider-cross" width="26" height="22" viewBox="0 0 26 22" aria-hidden="true">
      <line x1="2" y1="2" x2="24" y2="20" stroke="#1f1f1f" stroke-width="1.5"/>
      <line x1="24" y1="2" x2="2" y2="20" stroke="#1f1f1f" stroke-width="1.5"/>
    </svg>

    <section class="contact">
      <p class="phone">(816) 555-0193</p>
      <p class="email">peterwalsh@verdanthollow.com</p>
    </section>

    <section class="social">
      <p class="social-row"><span class="social-mark"></span>/VerdantHollowLawnandLandscape</p>
      <p class="social-row"><span class="social-mark"></span>/verdanthollow</p>
    </section>

    <div class="rule"><div class="rule-thick"></div><div class="rule-thin"></div></div>

    <p class="website">Verdanthollow.com</p>
  </article>
</main>
</body>
</html>
```